A4 Client Referral Program Flyer for Property Management Agency

Harbourline Lettings Group is a property management specialist based on Sydney's Northern Beaches in Australia.

We manage mid to high-end rental properties for investors and property owners.
We are currently looking to build our portfolio and are offering existing clients and contacts a referral incentive. We want to sign up more properties to manage.

We are offering the referrer a $250 referral fee and the new owner 2 months of free management to entice them to use Harbourline Lettings Group.

We want an A4 Flyer to print and add to other document packages we hand out to clients and suppliers.
If at all possible a matching digital banner would be great too! 1000px wide x 250px

Please find copy attached in Word Doc and our logo attached also.

Please see our website for any more details on our business.

We must be able to have an editable photoshop version (PSD) of the document as well as a print ready PDF version incl any bleed necessary for A4 printing.

Target Market(s)

30-60YO Male and Female

Industry/Entity Type

Real Estate

Font styles to use
Sans Serif

Requirements
Must have
• Company Logo, contact details and copy provided

```html
<!DOCTYPE html>
<html lang="en">
<head>
<meta charset="utf-8">
<title>Harbourline Lettings Group – Referral Program Flyer</title>
<link rel="stylesheet" href="https://fonts.googleapis.com/css2?family=Oswald:wght@400;500;600&family=Lato:wght@400;700&family=Montserrat:wght@700;800&display=swap">
<style>
  :root{
    --teal:#1d8a9c;
    --teal-light:#35b3c3;
    --teal-dark:#126a78;
    --charcoal:#222325;
    --ink:#333;
    --paper:#ffffff;
    --stage:#eeeeec;
    --sky-top:#2b8fd0;
    --sky-low:#bfe4f5;
    --leaf:#3f7a3a;
  }
  *{box-sizing:border-box;margin:0;padding:0}
  html,body{width:1200px;height:900px;overflow:hidden}
  body{background:var(--stage);font-family:"Lato",Arial,sans-serif;color:var(--ink)}
  .flyer{position:absolute;left:280px;top:20px;width:640px;height:860px;background:var(--paper);overflow:hidden;box-shadow:0 2px 10px rgba(0,0,0,.12)}
  .abs{position:absolute}
  .hero{left:0;top:0;width:640px;height:312px;background:linear-gradient(180deg,var(--sky-top) 0%,var(--sky-low) 30%,#9aa3a6 45%,#6b8a5a 70%,var(--leaf) 100%)}
  .shapes{left:0;top:0;width:640px;height:860px}
  .brand{right:26px;top:40px;font-family:"Lato",Arial,sans-serif;font-weight:700;font-size:19px;color:var(--charcoal);display:flex;align-items:center;gap:8px;letter-spacing:.5px}
  .brand-dot{width:12px;height:12px;border-radius:50%;background:var(--teal)}
  .about{left:22px;top:374px;width:302px}
  .about h2{font-family:"Lato",Arial,sans-serif;font-weight:400;font-size:14px;color:var(--teal);letter-spacing:.5px;margin-bottom:4px}
  .about p{font-size:8.6px;line-height:1.38;text-align:justify}
  .terms{left:22px;top:555px;width:302px;font-size:8.6px;line-height:1.38}
  .terms strong{font-size:11px}
  .url-bar{left:0;top:626px;width:334px;height:22px;background:var(--teal);color:#fff;font-family:"Lato",Arial,sans-serif;font-weight:700;font-size:10px;line-height:22px;padding-left:22px}
  .thumb{top:668px;width:116px;height:82px;border:2px solid var(--teal);padding:4px;background:#fff}
  .thumb div{width:100%;height:100%}
  .thumb-living{left:30px}
  .thumb-living div{background:linear-gradient(180deg,#e8ecef,#b9c7cf 60%,#6f8fa3)}
  .thumb-kitchen{left:188px}
  .thumb-kitchen div{background:linear-gradient(180deg,#f1f1ee,#d4d8d2 60%,#b6a9a2)}
  .offer{left:338px;top:400px;width:302px;text-align:center}
  .offer .invite{font-family:"Oswald",Arial,sans-serif;font-weight:500;font-size:31px;color:#fff;letter-spacing:.5px;line-height:1.05}
  .offer .receive{font-family:"Oswald",Arial,sans-serif;font-weight:500;font-size:27px;color:var(--teal-light);letter-spacing:2px;line-height:1.1}
  .offer .amount{font-family:"Oswald",Arial,sans-serif;font-weight:500;font-size:112px;color:#fff;line-height:1;margin-top:2px}
  .offer .months{font-family:"Oswald",Arial,sans-serif;font-weight:500;font-size:22px;color:var(--teal-light);letter-spacing:.5px;line-height:1.1;margin-top:6px}
  .offer .free{font-family:"Montserrat",Arial,sans-serif;font-weight:800;font-size:19px;color:#fff;letter-spacing:1px;line-height:1.2}
  .contacts{left:356px;top:660px;width:270px;font-size:8.2px;color:#ddd;line-height:1.65}
  .contact+.contact{margin-top:9px}
  .contact .name{color:var(--teal-light);font-weight:700}
  .contact .row{display:flex;align-items:center;gap:6px}
  .contact svg{width:7px;height:7px;flex:none}
  .footer-org{left:22px;top:786px;font-size:9.5px;line-height:1.45;color:#fff}
  .footer-org strong{display:block;font-size:10.5px;margin-bottom:2px}
  .footer-org .row{display:flex;gap:6px;align-items:center}
  .footer-org .line2{padding-left:13px}
  .footer-mail{left:235px;top:834px;font-size:9px;color:#fff;display:flex;gap:6px;align-items:center}
</style>
</head>
<body>
<main class="flyer">
  <div class="abs hero" role="img" aria-label="Photograph of modern terraced hillside homes with landscaped gardens under a blue sky"></div>

  <svg class="abs shapes" viewBox="0 0 640 860" aria-hidden="true">
    <polygon points="0,312 640,312 640,326 0,352" fill="var(--teal)"/>
    <polygon points="0,352 640,326 640,331 0,359" fill="var(--teal-light)"/>
    <polygon points="338,340 640,318 640,800 338,800" fill="var(--charcoal)"/>
    <polygon points="0,762 640,784 640,860 0,860" fill="var(--teal)"/>
    <polygon points="0,768 640,798 640,804 0,773" fill="#fff"/>
    <polygon points="0,773 640,804 640,808 0,776" fill="var(--teal-light)"/>
  </svg>

  <div class="abs brand"><span class="brand-dot"></span>HARBOURLINE LETTINGS GROUP</div>

  <section class="abs about">
    <h2>ABOUT US</h2>
    <p>Harbourline Lettings Group is a full service agency specializing in property management on Sydney's Northern Beaches.<br>
    We have a strong understanding of the local market, ensuring you get the best tenant, the best return and the highest quality of management and communication.<br>
    Property management is our core business and focus. You will get a professional, senior property manager looking after your property at all times.<br>
    We understand every owner/investor has different needs. Our aim is to personally tailor our services to satisfy those needs and ensure your experience with us is simple easy and confidence inspiring.</p>
  </section>

  <p class="abs terms"><strong>$250</strong> referral fee paid when the owner you refer signs their property for Management with Harbourline Lettings Group. Your referral must be submitted prior to signing on our website using the referral form on this page.</p>

  <div class="abs url-bar">http://www.harbourlinelettings.com.au/referral-program/</div>

  <div class="abs thumb thumb-living"><div role="img" aria-label="Photograph of a bright living room interior"></div></div>
  <div class="abs thumb thumb-kitchen"><div role="img" aria-label="Photograph of a modern kitchen with bar stools"></div></div>

  <section class="abs offer">
    <p class="invite">INVITE YOUR FRIENDS</p>
    <p class="receive">AND RECEIVE</p>
    <p class="amount">$250</p>
    <p class="months">AND THEY GET 2 MONTHS</p>
    <p class="free">FREE MANAGEMENT!</p>
  </section>

  <section class="abs contacts">
    <div class="contact">
      <div><span class="name">Tom Rawlings</span> – Director/Property Manager</div>
      <div class="row"><svg viewBox="0 0 10 10"><path d="M2 1l2 2-1 1.5c.8 1.5 1.8 2.5 3.5 3.5L8 7l2 2-1.5 1C4.5 10 0 5.5 1 1.5z" fill="var(--teal-light)"/></svg>0412 730 218</div>
      <div class="row"><svg viewBox="0 0 10 10"><circle cx="5" cy="5" r="4" fill="var(--teal-light)"/></svg>tom@harbourlinelettings.com.au</div>
    </div>
    <div class="contact">
      <div><span class="name">Lena Marsh</span> – Fixed By Lena, Maintenance and Repairs</div>
      <div class="row"><svg viewBox="0 0 10 10"><path d="M2 1l2 2-1 1.5c.8 1.5 1.8 2.5 3.5 3.5L8 7l2 2-1.5 1C4.5 10 0 5.5 1 1.5z" fill="var(--teal-light)"/></svg>0400 962 174</div>
      <div class="row"><svg viewBox="0 0 10 10"><circle cx="5" cy="5" r="4" fill="var(--teal-light)"/></svg>lena@fixedbylena.com.au</div>
    </div>
  </section>

  <div class="abs footer-org">
    <strong>Harbourline Lettings Group</strong>
    <div class="row"><svg width="7" height="9" viewBox="0 0 10 13"><path d="M5 0a5 5 0 0 1 5 5c0 3.5-5 8-5 8S0 8.5 0 5a5 5 0 0 1 5-5z" fill="#fff"/></svg>PO Box 214</div>
    <div class="line2">Seacliff Point, NSW 2099</div>
  </div>
  <div class="abs footer-mail"><svg width="9" height="9" viewBox="0 0 10 10"><circle cx="5" cy="5" r="4.5" fill="#fff"/></svg>info@harbourlinelettings.com.au</div>
</main>
</body>
</html>
```